sydney wedding photography business needs a business card design

we need a business card design for a sydney based wedding photography and videography business. our business name is :golden hour photography and video. our target clients are 24-35 yrs female. our style is candid, organic, natural, dynamic. we are a team of young photographers and videographers, and help brides to create memories that they will cherish for the rest of their lives. the logo will be provided. we want an elegant design that reflects our style, and also want to give a great impression to our clients that we are one of the best studios in sydney and our brand means quality and premium service.

Target Market(s)

bride to be, 24-35 years old, living in sydney and surrunding areas

Industry/Entity Type

Wedding Photography

Contact Information for Business Card

address: 57 marrow lane, bexton nsw 2041
mobile: 0431872056
phone: (02) 9361 2748
info@goldenhourstudio.net.au
www.goldenhourstudio.net.au
facebook:goldenhourbridals
instagram:goldenhourbridals

Font styles to use
Serif
Sans Serif

Requirements
Nice to have
• maybe add my slogan"memories beyond eternity" if the layout looks good
Should not have
• no black color, not good idea for wedding biz card

```html
<!DOCTYPE html>
<html lang="en">
<head>
<meta charset="utf-8">
<title>Golden Hour Photography and Video – Business Card</title>
<link rel="stylesheet" href="https://fonts.googleapis.com/css2?family=Roboto:wght@300;400;500&display=swap">
<style>
  :root {
    --page: #dedad3;
    --card-top: #faf6ee;
    --card-bottom: #efe6d5;
    --band: #e8dcc6;
    --gold: #b98d17;
    --icon-ink: #faf6ee;
    --ink: #4f4438;
    --ink-muted: #6e6152;
  }
  * { box-sizing: border-box; margin: 0; padding: 0; }
  html, body { width: 1200px; height: 1023px; overflow: hidden; }
  body {
    background: var(--page);
    font-family: "Roboto", Arial, sans-serif;
    position: relative;
  }
  .card {
    position: absolute;
    left: 260px;
    width: 680px;
    height: 416px;
    border-radius: 22px;
    background: linear-gradient(160deg, var(--card-top), var(--card-bottom));
    box-shadow: 0 10px 26px rgba(70, 55, 30, 0.22);
    overflow: hidden;
  }
  .card--back { top: 62px; }
  .card--front { top: 545px; }

  /* Wordmark */
  .wordmark {
    position: absolute;
    color: var(--gold);
    font-weight: 500;
    line-height: 1;
    white-space: nowrap;
  }
  .wordmark__name { display: block; }
  .wordmark__tag {
    display: block;
    text-transform: uppercase;
  }
  .card--back .wordmark { right: 56px; top: 66px; text-align: right; }
  .card--back .wordmark__name { font-size: 52px; }
  .card--back .wordmark__tag { font-size: 13px; letter-spacing: 0.4em; margin: 10px -0.4em 0 0; }

  .card--front .wordmark { left: 0; right: 0; top: 128px; text-align: center; }
  .card--front .wordmark__name { font-size: 74px; }
  .card--front .wordmark__tag { font-size: 17px; letter-spacing: 0.5em; margin: 16px -0.5em 0 0; }

  /* Contact block */
  .accent-line {
    position: absolute;
    height: 3px;
    background: var(--gold);
  }
  .accent-line--lead { left: 0; top: 226px; width: 236px; }
  .accent-line--end { left: 232px; top: 386px; width: 44px; }

  .contact-list {
    position: absolute;
    left: 238px;
    top: 246px;
    list-style: none;
  }
  .contact-list li {
    display: flex;
    align-items: center;
    height: 26px;
    color: var(--ink);
    font-size: 17px;
    font-weight: 400;
    letter-spacing: 0.02em;
  }
  .contact-list svg {
    width: 22px;
    height: 22px;
    margin-right: 14px;
    flex: none;
  }
  .icon-bg { fill: var(--gold); }
  .icon-fill { fill: var(--icon-ink); }
  .icon-stroke { fill: none; stroke: var(--icon-ink); }

  /* Social band */
  .social-band {
    position: absolute;
    left: 0;
    right: 0;
    bottom: 0;
    height: 52px;
    background: var(--band);
    display: flex;
    align-items: center;
    justify-content: space-between;
    padding: 0 40px;
  }
  .social-handle {
    display: flex;
    align-items: center;
    color: var(--ink-muted);
    font-size: 16px;
    font-weight: 400;
    letter-spacing: 0.03em;
  }
  .social-handle__mark {
    width: 14px;
    height: 14px;
    background: var(--gold);
    border-radius: 2px;
    margin-right: 10px;
  }
</style>
</head>
<body>

<section class="card card--back" aria-label="Business card, contact side">
  <div class="wordmark">
    <span class="wordmark__name">Golden Hour</span>
    <span class="wordmark__tag">Photography and Video</span>
  </div>

  <span class="accent-line accent-line--lead"></span>
  <ul class="contact-list">
    <li>
      <svg viewBox="0 0 22 22" aria-hidden="true"><circle class="icon-bg" cx="11" cy="11" r="11"/><path class="icon-fill" d="M7.5 6.5c.6-.5 1.3-.4 1.6.1l1 1.6c.3.5.2 1-.2 1.3l-.6.5c.5 1.1 1.4 2 2.5 2.5l.5-.6c.3-.4.9-.5 1.3-.2l1.6 1c.5.3.6 1 .1 1.6-.8.9-2 1.2-3.2.6-2.2-1.1-3.9-2.8-5-5-.6-1.2-.3-2.4.4-3.4z"/></svg>
      (02) 9361 2748
    </li>
    <li>
      <svg viewBox="0 0 22 22" aria-hidden="true"><circle class="icon-bg" cx="11" cy="11" r="11"/><rect class="icon-stroke" x="8" y="5.5" width="6" height="11" rx="1.2" stroke-width="1.4"/><circle class="icon-fill" cx="11" cy="14.4" r=".7"/></svg>
      0431872056
    </li>
    <li>
      <svg viewBox="0 0 22 22" aria-hidden="true"><circle class="icon-bg" cx="11" cy="11" r="11"/><rect class="icon-stroke" x="6" y="7.5" width="10" height="7" stroke-width="1.3"/><path class="icon-stroke" d="M6 7.5l5 4 5-4" stroke-width="1.3"/></svg>
      info@goldenhourstudio.net.au
    </li>
    <li>
      <svg viewBox="0 0 22 22" aria-hidden="true"><circle class="icon-bg" cx="11" cy="11" r="11"/><circle class="icon-stroke" cx="11" cy="11" r="5" stroke-width="1.2"/><path class="icon-stroke" d="M6 11h10M11 6c-2.2 2.8-2.2 7.2 0 10M11 6c2.2 2.8 2.2 7.2 0 10" stroke-width="1.1"/></svg>
      www.goldenhourstudio.net.au
    </li>
    <li>
      <svg viewBox="0 0 22 22" aria-hidden="true"><circle class="icon-bg" cx="11" cy="11" r="11"/><path class="icon-fill" d="M11 16.5s-4-4.2-4-7a4 4 0 0 1 8 0c0 2.8-4 7-4 7z"/><circle class="icon-bg" cx="11" cy="9.5" r="1.4"/></svg>
      57 marrow lane, bexton nsw 2041
    </li>
  </ul>
  <span class="accent-line accent-line--end"></span>
</section>

<section class="card card--front" aria-label="Business card, brand side">
  <div class="wordmark">
    <span class="wordmark__name">Golden Hour</span>
    <span class="wordmark__tag">Photography and Video</span>
  </div>
  <div class="social-band">
    <span class="social-handle"><span class="social-handle__mark"></span>goldenhourbridals</span>
    <span class="social-handle"><span class="social-handle__mark"></span>goldenhourbridals</span>
  </div>
</section>

</body>
</html>
```